Mine Engineering Consultancy specializing in
* Pit optimization
* Mine Design
* Scheduling
* Mine Rehabilitation

Industry/Entity Type

Mining

Contact Information for Business Card

RVT Mining Pty Ltd
Derek Holloway
Director/Principle Mining Engineer
Mobile 0413582961
Email derek.holloway@rvtmining-example.com

```html
<!DOCTYPE html>
<html lang="en">
<head>
<meta charset="utf-8">
<title>RVT Mining Pty Ltd – Business Card</title>
<link rel="stylesheet" href="https://fonts.googleapis.com/css2?family=Tinos:wght@400;700&family=Open+Sans:wght@400&display=swap">
<style>
  :root {
    --bg: #ecebe8;
    --card-white: #ffffff;
    --card-grey: #e9e9e9;
    --brand-blue: #2f5db0;
    --brand-blue-dark: #254c95;
    --ink: #1c1c1c;
    --ink-soft: #444444;
    --on-blue: #ffffff;
  }
  * { box-sizing: border-box; margin: 0; padding: 0; }
  html, body { width: 1200px; height: 900px; overflow: hidden; }
  body {
    background: var(--bg);
    position: relative;
    font-family: "Tinos", "Times New Roman", serif;
  }
  .card {
    position: absolute;
    left: 250px;
    width: 700px;
    height: 400px;
    overflow: hidden;
    box-shadow: 0 10px 28px rgba(0,0,0,0.22);
    background: var(--card-white);
  }
  .card--contact { top: 30px; border-radius: 0 70px 0 70px; }
  .card--services { top: 470px; border-radius: 70px 0 70px 0; }

  .texture {
    position: absolute;
    left: 0; right: 0;
    background: linear-gradient(180deg, var(--card-white) 0%, var(--card-grey) 100%);
  }

  .band {
    position: absolute;
    left: 0; right: 0;
    background: linear-gradient(180deg, var(--brand-blue) 0%, var(--brand-blue-dark) 100%);
  }

  /* Contact side */
  .card--contact .texture { top: 0; height: 230px; }
  .card--contact .band { top: 230px; bottom: 0; }
  .brand-dot {
    position: absolute;
    border-radius: 50%;
  }
  .card--contact .brand-dot {
    left: 50px; top: 60px; width: 110px; height: 110px;
    background: var(--brand-blue);
  }
  .company {
    position: absolute;
    font-weight: 400;
    white-space: nowrap;
  }
  .card--contact .company {
    right: 50px; top: 32px;
    font-size: 30px; color: var(--brand-blue);
  }
  .person-name {
    position: absolute; right: 50px; top: 82px;
    font-size: 26px; color: var(--ink);
  }
  .person-title {
    position: absolute; right: 50px; top: 170px;
    font-size: 27px; color: var(--ink);
  }
  .contact-line {
    position: absolute;
    display: flex; align-items: center; gap: 14px;
    font-family: "Open Sans", Arial, sans-serif;
    white-space: nowrap;
  }
  .contact-line svg { flex: none; }
  .card--contact .contact-line { color: var(--on-blue); font-size: 19px; }
  .card--contact .contact-phone { right: 60px; top: 262px; }
  .card--contact .contact-email { left: 50px; top: 334px; }

  /* Services side */
  .card--services .band { top: 0; height: 275px; }
  .card--services .texture { top: 275px; bottom: 0; }
  .headline {
    position: absolute; left: 70px; top: 22px;
    font-size: 29px; font-weight: 700; color: var(--ink);
    white-space: nowrap;
  }
  .card--services .brand-dot {
    left: 60px; top: 92px; width: 110px; height: 110px;
    background: var(--on-blue);
  }
  .card--services .company {
    left: 60px; top: 218px;
    font-size: 28px; color: var(--on-blue);
  }
  .services {
    position: absolute; left: 420px; top: 90px;
    list-style: none;
    font-size: 25px; color: var(--on-blue);
    line-height: 38px;
  }
  .services li::before { content: "* "; }
  .card--services .contact-line { color: var(--ink-soft); font-size: 18px; top: 318px; }
  .card--services .contact-email { left: 110px; }
  .card--services .contact-phone { left: 450px; top: 340px; }
</style>
</head>
<body>

<article class="card card--contact" aria-label="Business card, contact side">
  <div class="texture" role="img" aria-label="Light grey diamond texture background"></div>
  <div class="band"></div>
  <span class="brand-dot" aria-hidden="true"></span>
  <p class="company">RVT Mining Pty Ltd</p>
  <p class="person-name">Derek Holloway</p>
  <p class="person-title">Director/Principle Mining Engineer</p>
  <p class="contact-line contact-phone">
    <svg width="26" height="26" viewBox="0 0 24 24" aria-hidden="true"><path fill="#1c1c1c" d="M6.6 10.8a15.1 15.1 0 0 0 6.6 6.6l2.2-2.2c.3-.3.7-.4 1-.2 1.1.4 2.3.6 3.6.6.6 0 1 .4 1 1V20c0 .6-.4 1-1 1A17 17 0 0 1 3 4c0-.6.4-1 1-1h3.5c.6 0 1 .4 1 1 0 1.3.2 2.5.6 3.6.1.3 0 .7-.2 1z"/></svg>
    0413582961
  </p>
  <p class="contact-line contact-email">
    <svg width="34" height="24" viewBox="0 0 34 24" aria-hidden="true"><rect x="1" y="1" width="32" height="22" fill="#1c1c1c"/><path d="M1 1l16 12L33 1" fill="none" stroke="#ffffff" stroke-width="2"/></svg>
    derek.holloway@rvtmining-example.com
  </p>
</article>

<article class="card card--services" aria-label="Business card, services side">
  <div class="band"></div>
  <div class="texture" role="img" aria-label="Light grey diamond texture background"></div>
  <h1 class="headline">Mine Engineering Consultancy specializing:-</h1>
  <span class="brand-dot" aria-hidden="true"></span>
  <p class="company">RVT Mining Pty Ltd</p>
  <ul class="services">
    <li>Pit optimization</li>
    <li>Mine Design</li>
    <li>Scheduling</li>
    <li>Mine Rehabilitation</li>
  </ul>
  <p class="contact-line contact-email">
    <svg width="36" height="26" viewBox="0 0 34 24" aria-hidden="true"><rect x="1" y="1" width="32" height="22" fill="#2f5db0"/><path d="M1 1l16 12L33 1" fill="none" stroke="#ffffff" stroke-width="2"/></svg>
    derek.holloway@rvtmining-example.com
  </p>
  <p class="contact-line contact-phone">
    <svg width="30" height="30" viewBox="0 0 24 24" aria-hidden="true"><path fill="#2f5db0" d="M6.6 10.8a15.1 15.1 0 0 0 6.6 6.6l2.2-2.2c.3-.3.7-.4 1-.2 1.1.4 2.3.6 3.6.6.6 0 1 .4 1 1V20c0 .6-.4 1-1 1A17 17 0 0 1 3 4c0-.6.4-1 1-1h3.5c.6 0 1 .4 1 1 0 1.3.2 2.5.6 3.6.1.3 0 .7-.2 1z"/></svg>
    0413582961
  </p>
</article>

</body>
</html>
```